Website for small historic hotel called the Corbett Crown

We are looking to design a website for a small Inn/Hotel.
Site would need to be able to take reservations and flow through to booking via Tallypay with orchard pay, quorra pay and zunmi pay (Chinese verson )
We would have links from Velora, Vorbo.com, roam critic etc to our website for booking purposes
Here are some examples of small inn/hotels doing the same sort of thing in our area. Provided purely for reference, not to be plagiarized!
https://innbrackwell.example/tollivers/
https://www.dunmorecourt.example/hotel
https://www.falconinnbrackwell.example/hotel
https://www.thewendover.example/
We will also provide you some photos, once the site has been done, to utilize instead of random shots taken from the internet as placeholders
I have also provided a link to some hotels in Perthshire Scotland which may also provide you with some ideas Again please do not plagiarise
https://glenvarrowlodge.example/
https://www.theinnatcraigbrannoch.example/
https://www.fennickheadhotel.example/
http://www.northern-hostelries.example/HighlandsandBorders.htm
Our inn is in Perth County in Ontario Canada NOT Scotland but the original owner was a Corbett from Perthshire Scotland and is responsible for the county being named Perth
We would need a landing page plus the following
page for rooms
Page for booking
Contact page
About US Page
Total site is landing page plus 4 or 5 sub pages
The general outline is provided. Please contact me with specific questions
Just as an update the folllowing are the placeholder names for the pages. They will be tabs at the top right and fllow through to sub pages off the main landing page
MAIN LANDING PAGE links at top to
1 _ history - the story of the building and Corbett
2_ Contact
3_ Rooms and Suites - will have each room and suite and link to sub-page for each
4 _ Perth County
5 - to be determined
The following would be sub pages
3 will display links to the suites: with a sub-page for each suite
Garden Suite - includes a 500 square foot patio and garden
Reception Suite - under renovation
Parlour Suite - Old parlor - Under renovation
GRAYMOORHAVEN Suite - Under renovation
1854 Suite 0- Under renovation
Updates
Just some additional information
The Inn/Hotel this website is for is named after a native of Perthshire Scotland who is also responsible for the area being names Perth County
The building is constructed in the 1850's and the decor and design are those of small-town inns you can find in the British Isles - England, Scotonal, Ireland and Wales
Some examples from Perthshire in Scotland - for inspiration, not plagiarisation!
https://glenvarrowlodge.example/
Please note the inn does not have a restaurant at present and only offers rooms
Feel free to submitt any questions for clarification
I have also provided a link to some hotels in Perthshire Scotland with similar designs and crests as well as to give you some background as to Perth. Again please do not plagiarise
https://glenvarrowlodge.example/
This is provided as an outline and we can answer specific questions
Few if any designs of any quality were received. Really nowhere near what was promised and certainly not the quality or quantity I would expect KT, whom I worked with before and I invited, submitted the bulk of the entries
Industry/Entity Type
boutique hotel - 19th century traditional British Isles
Number of Pages Required
5+ page
Look and feel
Each slider illustrates characteristics of the customer's brand and the style your logo design should communicate.

```html
<!DOCTYPE html>
<html lang="en">
<head>
<meta charset="utf-8">
<title>Corbett Crown</title>
<link rel="stylesheet" href="https://fonts.googleapis.com/css2?family=Montserrat:wght@400;500;600;700&family=Libre+Baskerville:wght@700&display=swap">
<style>
:root{
  --orange:#f47a2a;
  --ink:#1d1d1d;
  --muted:#555;
  --line:#dcdcdc;
  --grey-bg:#f4f3f3;
  --white:#fff;
  --footer:#232323;
  --panel:#eef5fb;
}
*{box-sizing:border-box;margin:0;padding:0}
html,body{width:1200px;height:3484px;overflow:hidden}
body{position:relative;font-family:'Montserrat',sans-serif;color:var(--ink);background:var(--white)}
a{text-decoration:none;color:inherit}
.photo{position:absolute}

/* ticks */
.ticks li{list-style:none;display:flex;align-items:center;gap:10px}
.ticks li::before{content:"";flex:none;width:4px;height:8px;border-right:2px solid var(--orange);border-bottom:2px solid var(--orange);transform:rotate(45deg);margin:-3px 2px 0 2px}

/* header */
.site-header{position:absolute;top:0;left:0;width:1200px;height:65px;background:var(--white);z-index:3}
.wordmark{position:absolute;left:133px;top:21px;font-size:18px;font-weight:600;color:var(--ink);letter-spacing:.5px}
.main-nav{position:absolute;top:22px;left:597px;display:flex;align-items:center;font-size:15px}
.main-nav a{margin-right:34px}
.main-nav a.active{color:var(--orange);text-decoration:underline;text-underline-offset:4px}
.btn-nav{position:absolute;left:966px;top:19px;width:103px;height:28px;background:var(--orange);color:var(--white);font-size:15px;display:flex;align-items:center;justify-content:center}

/* hero */
.hero{position:absolute;top:65px;left:0;width:1200px;height:500px;background:linear-gradient(180deg,#2f6bbf 0%,#6fa3dc 45%,#b8cde0 70%,#5d6c7c 88%,#4a5a52 100%)}
.hero-welcome{position:absolute;left:187px;top:284px;font-size:25px;color:#2b2b2b;font-weight:500}
.hero-title{position:absolute;left:187px;top:312px;font-family:'Libre Baskerville',serif;font-size:52px;color:#222}
.book-panel{position:absolute;left:755px;top:142px;width:314px;height:295px;background:var(--panel);padding:22px 20px}
.book-panel h2{font-size:18px;font-weight:600;margin-bottom:14px}
.field-label{font-size:11px;margin-bottom:6px}
.field{height:36px;background:var(--white);border:1px solid #aaa;font-size:10px;color:#666;display:flex;align-items:center;justify-content:space-between;padding:0 10px;margin-bottom:14px}
.selects{display:flex;gap:10px;margin-bottom:13px}
.selects .field{flex:1;margin:0;padding:0 8px}
.btn-search{height:40px;background:var(--orange);color:var(--white);font-weight:700;font-size:18px;display:flex;align-items:center;justify-content:center}

/* headings */
.section-title{position:absolute;left:0;width:1200px;text-align:center;font-size:19px;font-weight:700}
.section-title::after{content:"";display:block;width:66px;height:2px;background:var(--orange);margin:20px auto 0}

/* cards */
.card{position:absolute;top:693px;width:300px;height:396px;background:var(--white);box-shadow:0 2px 12px rgba(0,0,0,.08)}
.card .photo{left:0;top:0;width:300px;height:183px}
.card-body{position:absolute;top:200px;left:19px;right:19px}
.card h3{font-size:15px;font-weight:600}
.card .loc{font-size:10.5px;color:var(--muted);margin-top:4px}
.card p{font-size:10.5px;line-height:16px;color:#333;margin-top:13px}
.rates{display:flex;gap:10px;margin-top:12px}
.rate{width:80px;height:52px;border:1px solid var(--line);text-align:center;font-size:11px;padding-top:9px}
.rate .n{font-size:11px;font-weight:600;color:#555;display:block;margin-bottom:6px}

/* listing */
.listing{position:absolute;top:1139px;left:0;width:1200px;height:1283px;background:var(--grey-bg)}
.row{position:absolute;left:133px;width:937px;height:203px;background:var(--white);box-shadow:0 1px 6px rgba(0,0,0,.05)}
.row .photo{left:19px;top:19px;width:252px;height:164px}
.row h3{position:absolute;left:301px;top:24px;font-size:16px;font-weight:600}
.row .loc{position:absolute;left:301px;top:49px;font-size:10.5px;font-weight:500}
.feats{position:absolute;left:303px;top:80px;display:grid;grid-template-columns:160px 200px;font-size:10.5px;row-gap:4px}
.row-rates{position:absolute;right:25px;top:31px;width:161px}
.row-rate{display:flex;height:40px;border:1px solid var(--line);margin-bottom:12px}
.row-rate .n{width:75px;border-right:1px solid var(--line);display:flex;align-items:center;justify-content:center;font-size:11px;font-weight:600;color:#555}
.row-rate .p{flex:1;display:flex;align-items:center;justify-content:center;font-size:15px;font-weight:500}
.btn-more{position:absolute;left:515px;top:1207px;width:170px;height:36px;background:var(--orange);color:var(--white);font-size:13px;font-weight:700;display:flex;align-items:center;justify-content:center}

/* facilities */
.fac-title{position:absolute;left:787px;top:2493px;font-size:20px;font-weight:700}
.fac-title::after{content:"";display:block;width:40px;height:2px;background:var(--orange);margin-top:14px}
.fac-list{position:absolute;left:791px;top:2550px;font-size:14.5px}
.fac-list li{height:27.2px}

/* cta */
.cta{position:absolute;top:3006px;left:0;width:1200px;height:302px;background:linear-gradient(90deg,#3a3733 0%,#5b5650 40%,#b9b2a8 75%,#d6cfc4 100%)}
.cta-shade{position:absolute;inset:0;background:rgba(0,0,0,.25)}
.cta-text{position:absolute;top:80px;left:0;width:1200px;text-align:center;color:var(--white);font-size:23px;font-weight:700;line-height:34px}
.btn-cta{position:absolute;left:515px;top:173px;width:168px;height:49px;background:var(--orange);color:var(--white);font-weight:700;font-size:16px;display:flex;align-items:center;justify-content:center}

/* footer */
.site-footer{position:absolute;top:3308px;left:0;width:1200px;height:176px;background:var(--footer);color:var(--white)}
.foot-wordmark{position:absolute;left:133px;top:76px;font-size:18px;font-weight:600;letter-spacing:.5px}
.foot-nav{position:absolute;top:39px;right:131px;display:flex;gap:38px;font-size:15px}
.pay{position:absolute;top:85px;right:131px;display:flex;align-items:center;gap:22px;font-size:13px}
.pay .m{font-size:16px;font-weight:600}
.copy{position:absolute;top:132px;right:131px;font-size:13px}
</style>
</head>
<body>

<header class="site-header">
  <a class="wordmark" href="#">Corbett Crown</a>
  <nav class="main-nav">
    <a class="active" href="#">Home</a><a href="#">About Us</a><a href="#">Hotels</a><a href="#">Contact Us</a>
  </nav>
  <a class="btn-nav" href="#">Book Now</a>
</header>

<section class="hero" role="img" aria-label="City skyline with a tall tower under a blue sky"></section>
<div class="hero-welcome">Welcome to</div>
<h1 class="hero-title">Corbett Crown</h1>

<form class="book-panel">
  <h2>Book Now</h2>
  <div class="field-label">Check-in date</div>
  <div class="field"><span>dd/mm/yyyy</span><span>▭</span></div>
  <div class="field-label">Check-out date</div>
  <div class="field"><span>dd/mm/yyyy</span><span>▭</span></div>
  <div class="selects">
    <div class="field"><span>Adults</span><span>▾</span></div>
    <div class="field"><span>Children</span><span>▾</span></div>
    <div class="field"><span>Rooms</span><span>▾</span></div>
  </div>
  <div class="btn-search">SEARCH</div>
</form>

<h2 class="section-title" style="top:614px">ONTARIO CANADA HOTELS NEAR PERTH COUNTY</h2>

<article class="card" style="left:130px">
  <div class="photo" role="img" aria-label="Bedroom with a patterned quilt" style="background:linear-gradient(135deg,#c9c1ad,#8a8275)"></div>
  <div class="card-body">
    <h3>Lorem Ipsum is simply dummy</h3><div class="loc">Perth County</div>
    <p>Each spacious guest room comes equipped with a flat-screen HDTV, coffee maker, hairdryer, seating area and work desk.</p>
    <div class="rates"><div class="rate"><span class="n">velora</span>$145.99</div><div class="rate"><span class="n">vorbo.com</span>$85.99</div><div class="rate"><span class="n">roam critic</span>$105.99</div></div>
  </div>
</article>
<article class="card" style="left:449px">
  <div class="photo" role="img" aria-label="Dining room with a round wooden table" style="background:linear-gradient(135deg,#8b8072,#3e362f)"></div>
  <div class="card-body">
    <h3>Lorem Ipsum is simply dummy</h3><div class="loc">Perth County</div>
    <p>Each spacious guest room comes equipped with a flat-screen HDTV, coffee maker, hairdryer, seating area and work desk.</p>
    <div class="rates"><div class="rate"><span class="n">velora</span>$145.99</div><div class="rate"><span class="n">vorbo.com</span>$85.99</div><div class="rate"><span class="n">roam critic</span>$105.99</div></div>
  </div>
</article>
<article class="card" style="left:768px">
  <div class="photo" role="img" aria-label="Patio with table, chairs and umbrella" style="background:linear-gradient(135deg,#b6d8c6,#6f7c74)"></div>
  <div class="card-body">
    <h3>Lorem Ipsum is simply dummy</h3><div class="loc">Perth County</div>
    <p>Each spacious guest room comes equipped with a flat-screen HDTV, coffee maker, hairdryer, seating area and work desk.</p>
    <div class="rates"><div class="rate"><span class="n">velora</span>$145.99</div><div class="rate"><span class="n">vorbo.com</span>$85.99</div><div class="rate"><span class="n">roam critic</span>$105.99</div></div>
  </div>
</article>

<section class="listing">
  <h2 class="section-title" style="top:33px">HOTELS &amp; INNS IN ONTARIO CANADA</h2>

  <article class="row" style="top:107px">
    <div class="photo" role="img" aria-label="Hotel tower beside a pool" style="background:linear-gradient(180deg,#5d97d9,#c7d4de 60%,#3b8fa8)"></div>
    <h3>Lorem Ipsum is simply dummy</h3><div class="loc">Perth County</div>
    <ul class="feats ticks"><li>Picnic area</li><li>Designated smoking area</li><li>Outdoor furniture</li><li>Air conditioning</li><li>Fire extinguishers</li><li>Hardwood or parquet floors</li><li>CCTV outside property</li><li>Heating</li><li>Flat-screen TV</li><li>Pets are allowed</li></ul>
    <div class="row-rates"><div class="row-rate"><span class="n">velora</span><span class="p">$145.99</span></div><div class="row-rate"><span class="n">vorbo.com</span><span class="p">$125.99</span></div><div class="row-rate"><span class="n">roam critic</span><span class="p">$115.99</span></div></div>
  </article>

  <article class="row" style="top:323px">
    <div class="photo" role="img" aria-label="White modern hotel building against blue sky" style="background:linear-gradient(135deg,#3d8fe0,#dfe6ee 60%,#b5bcc4)"></div>
    <h3>Lorem Ipsum is simply dummy</h3><div class="loc">Perth County</div>
    <ul class="feats ticks"><li>Picnic area</li><li>Designated smoking area</li><li>Outdoor furniture</li><li>Air conditioning</li><li>Fire extinguishers</li><li>Hardwood or parquet floors</li><li>CCTV outside property</li><li>Heating</li><li>Flat-screen TV</li><li>Pets are allowed</li></ul>
    <div class="row-rates"><div class="row-rate"><span class="n">velora</span><span class="p">$145.99</span></div><div class="row-rate"><span class="n">vorbo.com</span><span class="p">$125.99</span></div><div class="row-rate"><span class="n">roam critic</span><span class="p">$115.99</span></div></div>
  </article>

  <article class="row" style="top:543px">
    <div class="photo" role="img" aria-label="Resort towers with palm trees and pool" style="background:linear-gradient(180deg,#d7e3ee,#8fa58a 60%,#2f6a5a)"></div>
    <h3>Lorem Ipsum is simply dummy</h3><div class="loc">Port Loring</div>
    <ul class="feats ticks"><li>Picnic area</li><li>Designated smoking area</li><li>Outdoor furniture</li><li>Air conditioning</li><li>Fire extinguishers</li><li>Hardwood or parquet floors</li><li>CCTV outside property</li><li>Heating</li><li>Flat-screen TV</li><li>Pets are allowed</li></ul>
    <div class="row-rates"><div class="row-rate"><span class="n">velora</span><span class="p">$145.99</span></div><div class="row-rate"><span class="n">vorbo.com</span><span class="p">$125.99</span></div><div class="row-rate"><span class="n">roam critic</span><span class="p">$115.99</span></div></div>
  </article>

  <article class="row" style="top:758px">
    <div class="photo" role="img" aria-label="Bedroom with tall windows and city view" style="background:linear-gradient(135deg,#2f3a48,#8f8a82 60%,#c9c4bc)"></div>
    <h3>Lorem Ipsum is simply dummy</h3><div class="loc">Perth County</div>
    <ul class="feats ticks"><li>Picnic area</li><li>Designated smoking area</li><li>Outdoor furniture</li><li>Air conditioning</li><li>Fire extinguishers</li><li>Hardwood or parquet floors</li><li>CCTV outside property</li><li>Heating</li><li>Flat-screen TV</li><li>Pets are allowed</li></ul>
    <div class="row-rates"><div class="row-rate"><span class="n">velora</span><span class="p">$145.99</span></div><div class="row-rate"><span class="n">vorbo.com</span><span class="p">$125.99</span></div><div class="row-rate"><span class="n">roam critic</span><span class="p">$115.99</span></div></div>
  </article>

  <article class="row" style="top:971px">
    <div class="photo" role="img" aria-label="White bedroom with blue cushions and curtains" style="background:linear-gradient(135deg,#2a52b8,#f1f1f3 45%,#d9dbe2)"></div>
    <h3>Lorem Ipsum is simply dummy</h3><div class="loc">Perth County</div>
    <ul class="feats ticks"><li>Picnic area</li><li>Designated smoking area</li><li>Outdoor furniture</li><li>Air conditioning</li><li>Fire extinguishers</li><li>Hardwood or parquet floors</li><li>CCTV outside property</li><li>Heating</li><li>Flat-screen TV</li><li>Pets are allowed</li></ul>
    <div class="row-rates"><div class="row-rate"><span class="n">velora</span><span class="p">$145.99</span></div><div class="row-rate"><span class="n">vorbo.com</span><span class="p">$125.99</span></div><div class="row-rate"><span class="n">roam critic</span><span class="p">$115.99</span></div></div>
  </article>

  <a class="btn-more" href="#">VIEW MORE HOTELS</a>
</section>

<div class="photo" role="img" aria-label="Kitchen with white cabinets and steel appliances" style="left:133px;top:2468px;width:335px;height:335px;background:linear-gradient(160deg,#e7e6e2,#8d8c89 60%,#3e3b37)"></div>
<div class="photo" role="img" aria-label="Sitting corner with two antique chairs" style="left:486px;top:2468px;width:254px;height:128px;background:linear-gradient(135deg,#b7b7a8,#6f6b5e)"></div>
<div class="photo" role="img" aria-label="Tiled shower with steel panel" style="left:486px;top:2618px;width:254px;height:331px;background:linear-gradient(160deg,#a8a49f,#6b6763)"></div>
<div class="photo" role="img" aria-label="Garden patio beside a mint green wall" style="left:133px;top:2821px;width:335px;height:128px;background:linear-gradient(90deg,#a9d9c2,#5f6d58 55%,#d9d9d4)"></div>

<h2 class="fac-title">FACILITIES</h2>
<ul class="fac-list ticks">
  <li>Designated smoking area</li><li>Air conditioning</li><li>Hypoallergenic room available</li><li>Hardwood or parquet floors</li><li>Heating</li><li>Private entrance</li><li>Carpeted</li><li>Family rooms</li><li>Facilities for disabled guests</li><li>Non-smoking rooms</li><li>Outdoor furniture</li><li>Barbecue</li><li>BBQ facilities</li><li>Garden</li>
</ul>

<section class="cta" role="img" aria-label="Bedroom with lamp and tree-patterned bedding">
  <div class="cta-shade"></div>
  <p class="cta-text">LOREM IPSUM IS SIMPLY DUMMY TEXT OF THE<br>PRINTING AND TYPESETTING INDUSTRY</p>
  <a class="btn-cta" href="#">BOOK NOW</a>
</section>

<footer class="site-footer">
  <div class="foot-wordmark">Corbett Crown</div>
  <nav class="foot-nav"><a href="#">Home</a><a href="#">About Us</a><a href="#">Hotels</a><a href="#">Contact Us</a></nav>
  <div class="pay"><span>Booking via</span><span class="m">orchard pay</span><span class="m">quorra pay</span><span class="m">zunmi pay</span></div>
  <div class="copy">Copyright © 2022 All Rights Reserved</div>
</footer>

</body>
</html>
```